Stroke Nine Indoor Rowing Center Website

We need a very clean, professional and appealing website for a new company based in Avon, CT (USA) called "Stroke Nine Indoor Rowing Center." Basically, this company as implied by its name is an indoor rowing center that consists of indoor rowing machines (Vantor 7 ergometers, http://www.vantor7.example) and a rowing simulator (called a "glidevator", (http://www.oarmakerlabs.example). These ergometers and simulators will in turn be interfaced with visualization and analysis software (www.pulsewaterly.example) to display "virtual" races and training sessions.

Ultimately, the company will also offer advanced video analysis and 1-1 coaching, but the key message here is to leverage off the company name "Stroke Nine" (which is a term for taking 10 very hard strokes during a rowing race) and the tagline that describes the company ("Indoor Rowing Center").

We have just completed a contest to establish the company's new logo (which I am attaching to this application) and we have some other photos that we think would be helpful in visually describing the company and its services (which I will also attach).

Part of what we like about he logo we selected are the color patterns (which will contrast nicely on both light and dark backgrounds) and the way the concept of a rower is built into the name. In addition, I like the way the number 10 subtly implies IO (as in "input and output" and/or binary numbers to also indicate a "technological dimension" to the company's services).

Also, one of the websites that we really like (that offers a similar progarm and service) in the New York City area is: http://www.harbin-oars.example. The site is clean, informative and easy to navigate. In terms of pages, we'd be looking for the following:

Home
Info (with sub pages for About, Code of Conduct, Experience the Difference, and Careers)
Coaches
Programs*
Blog
Contact
Donate!

*Note that the various programs will be offered and managed through a third-party tool (www.skullhubly.example) and (https://wiki.skullhubly.example/display/FAQ/FAQs#FAQs-WhatfeaturesareavailablethroughyourClubManagementservice%3F) to allow clients to register, sign an electronic waiver and pay for programs and annual memberships. An example of these links is also available at another popular rowing web page, Tidewell Sculling in Boston, MA (https://www.tidewellsculling.example/signup/) or possibly another sign up service called "ZenTrack" (https://www.zentrackhub.example/?ql=softwrfooter)

Finally, we would also like to have links in the navigation bar to connect to social networking sites like Chatterloop, WorkLattice, Quorvo+, etc.

Lastly, I realize that ArtFlock specializes in design only, but we would be interested in receiving estimates for a "turn-key" project that would include coding (or if there are specific partners your design firm works with to codify your designs).

Please let me know if you have any questions or if I can provide any additional information.

Thank you!

Dale

Target Market(s)

Please refer to the attached Powerpoint document for information about target market and the company's vision and mission.

Industry/Entity Type

Electronic

Requirements
Must have
• Clean, intuitive, highly visual and professional look and feel. A color patter and "style guide" that works effectively with the colors and design of our logo that we can build off of as we have new content.

```html
<!DOCTYPE html>
<html lang="en">
<head>
<meta charset="utf-8">
<title>Stroke Nine Indoor Rowing Center</title>
<link rel="stylesheet" href="https://fonts.googleapis.com/css2?family=Hind:wght@300;400;500;600&display=swap">
<style>
  :root {
    --orange: #ef6a1f;
    --orange-deep: #e0760f;
    --orange-light: #f7a030;
    --mauve: #8f7b88;
    --mauve-dark: #6e5465;
    --plum: #5f4456;
    --ink: #3a3a3a;
    --grey-text: #555;
    --white: #ffffff;
  }
  * { box-sizing: border-box; margin: 0; padding: 0; }
  html, body { width: 1200px; height: 1008px; overflow: hidden; }
  body {
    font-family: "Hind", "Helvetica Neue", Arial, sans-serif;
    background: #fbfbfb;
    position: relative;
    color: var(--ink);
  }

  /* Header */
  .site-header {
    position: absolute; left: 0; top: 0; width: 1200px; height: 120px;
    background: linear-gradient(#f2f2f2, #ffffff 40%);
  }
  .brand { position: absolute; left: 110px; top: 22px; }
  .brand-name {
    display: flex; align-items: center; gap: 10px;
    font-size: 50px; font-weight: 600; color: var(--orange);
    line-height: 1; letter-spacing: -1px;
  }
  .brand-mark { width: 14px; height: 14px; background: var(--mauve); }
  .brand-tagline {
    margin-top: 8px; font-size: 14px; font-weight: 600; letter-spacing: 3.2px;
    color: #222;
  }
  .social { position: absolute; left: 934px; top: 18px; display: flex; gap: 6px; }
  .social a {
    width: 34px; height: 34px; border-radius: 50%;
    background: radial-gradient(circle at 50% 40%, #9a8493, var(--mauve-dark));
    border: 2px solid #e8e3e6; display: block;
  }
  .search {
    position: absolute; left: 855px; top: 71px; width: 234px; height: 32px;
    border: 1px solid #d4d4d4; background: #fff;
    font-size: 13px; color: #888; padding: 8px 11px; line-height: 1.2;
  }
  .search svg { position: absolute; right: 11px; top: 8px; }

  /* Navigation */
  .main-nav {
    position: absolute; left: 0; top: 120px; width: 1200px; height: 45px;
    background: linear-gradient(#9a8693, var(--mauve));
    border-top: 1px solid #b7a8b2;
  }
  .main-nav ul { list-style: none; display: flex; position: absolute; left: 109px; top: 0; height: 45px; border-left: 1px solid #b5a7b0; }
  .main-nav li {
    height: 45px; line-height: 47px; text-align: center; color: var(--white);
    font-size: 16px; border-right: 1px solid #b5a7b0;
  }
  .main-nav li.current { background: linear-gradient(#7a6072, #9a8494); font-weight: 500; }
  .main-nav li.donate { background: linear-gradient(var(--orange-light), var(--orange-deep)); }

  /* Hero */
  .hero {
    position: absolute; left: 0; top: 165px; width: 1200px; height: 468px;
    background: linear-gradient(100deg, #5d5556 0%, #8a7c78 30%, #6d7a86 55%, #4e8fa8 75%, #7d6f6c 100%);
  }
  .hero-title {
    position: absolute; left: 110px; top: 142px; height: 45px; padding: 0 10px;
    background: rgba(120, 90, 110, .85); color: #fff; font-size: 27px; font-weight: 400; line-height: 50px;
  }
  .hero-copy {
    position: absolute; left: 110px; top: 206px; width: 460px;
    color: #fff; font-size: 15.5px; line-height: 22px;
  }
  .hero-button {
    position: absolute; left: 108px; top: 336px; width: 353px; height: 64px;
    border: 4px solid rgba(255,255,255,.55); border-radius: 3px;
    background: linear-gradient(var(--orange-light), var(--orange-deep));
    color: #fff; font-size: 27px; text-align: center; line-height: 62px;
  }
  .slide-arrow { position: absolute; }
  .slide-arrow.prev { left: 38px; top: 186px; }
  .slide-arrow.next { left: 1108px; top: 186px; }
  .hero-shadow {
    position: absolute; left: 0; top: 633px; width: 1200px; height: 50px;
    background: linear-gradient(rgba(0,0,0,.18), rgba(0,0,0,0));
  }

  /* Intro */
  .intro-title {
    position: absolute; left: 0; top: 704px; width: 1200px; text-align: center;
    color: var(--orange); font-size: 33px; font-weight: 300; letter-spacing: -.2px;
  }
  .intro-sub {
    position: absolute; left: 0; top: 754px; width: 1200px; text-align: center;
    color: var(--grey-text); font-size: 21px; font-weight: 300;
  }

  /* Product cards */
  .product {
    position: absolute; top: 799px; width: 304px; height: 164px;
    border-radius: 4px; overflow: hidden; color: #fff;
    background: linear-gradient(var(--plum), #8d7887);
    box-shadow: 0 12px 14px -10px rgba(0,0,0,.35);
  }
  .product.featured { background: linear-gradient(var(--orange-deep), var(--orange-light)); }
  .product h3 { position: absolute; left: 20px; top: 14px; font-size: 26px; font-weight: 500; }
  .product p { position: absolute; left: 20px; top: 53px; width: 170px; font-size: 14px; line-height: 18px; }
  .product-photo { position: absolute; right: 0; top: 0; width: 109px; height: 164px; }
</style>
</head>
<body>
  <header class="site-header">
    <div class="brand">
      <div class="brand-name"><span>Stroke Nine</span><span class="brand-mark"></span></div>
      <div class="brand-tagline">INDOOR ROWING CENTER</div>
    </div>
    <nav class="social" aria-label="Social networks">
      <a href="#" aria-label="Chatterloop"></a>
      <a href="#" aria-label="Scrollnest"></a>
      <a href="#" aria-label="WorkLattice"></a>
      <a href="#" aria-label="Quorvo+"></a>
    </nav>
    <div class="search">Search
      <svg width="18" height="16" viewBox="0 0 18 16"><circle cx="6.5" cy="6.5" r="5" fill="none" stroke="#999" stroke-width="2"/><line x1="10" y1="10" x2="16" y2="14" stroke="#999" stroke-width="3" stroke-linecap="round"/></svg>
    </div>
  </header>

  <nav class="main-nav">
    <ul>
      <li style="width:110px">Home</li>
      <li class="current" style="width:138px">About Us</li>
      <li style="width:120px">Careers</li>
      <li style="width:122px">Coaches</li>
      <li style="width:132px">Programs</li>
      <li style="width:102px">Blog</li>
      <li style="width:140px">Contact Us</li>
      <li class="donate" style="width:114px">Donate</li>
    </ul>
  </nav>

  <section class="hero" role="img" aria-label="Photo of a group of women training side by side on indoor rowing machines">
    <svg class="slide-arrow prev" width="52" height="52" viewBox="0 0 52 52"><circle cx="26" cy="26" r="25" fill="#c2703a" opacity=".55"/><path d="M32 14 L16 26 L32 38 Z" fill="#e6c6b2" opacity=".8"/></svg>
    <h1 class="hero-title">Best coaching platform in the world</h1>
    <p class="hero-copy">With a choice of the Glide A, Glide B, or Flux, pick the indoor rower that best suits you. Record, track and compare your times with athletes around the world.</p>
    <div class="hero-button">MORE INFORMATION</div>
    <svg class="slide-arrow next" width="52" height="52" viewBox="0 0 52 52"><circle cx="26" cy="26" r="24" fill="var(--orange)" stroke="#fff" stroke-width="2"/><path d="M20 13 L37 26 L20 39 Z" fill="#fff"/></svg>
  </section>
  <div class="hero-shadow"></div>

  <h2 class="intro-title">FIND OUT WHY OUR PRODUCTS ARE USED BY ATHLETES EVERYWHERE</h2>
  <p class="intro-sub">Lorem Ipsum is simply dummy text of the printing and typesetting industry.</p>

  <article class="product" style="left:110px">
    <h3>Indoor Rowers</h3>
    <p>Lorem Ipsum is simply dummy text of the printing and type setting industry. Lorem Ipsum has been the industry's</p>
    <div class="product-photo" role="img" aria-label="Photo of an athlete on an indoor rower" style="background:linear-gradient(#d8d4cc,#6a6866)"></div>
  </article>
  <article class="product featured" style="left:446px">
    <h3>Oars</h3>
    <p>Lorem Ipsum is simply dummy text of the printing and type setting industry. Lorem Ipsum has been the industry's</p>
    <div class="product-photo" role="img" aria-label="Photo of yellow oar blades lying in grass" style="background:linear-gradient(90deg,#5d6a2c,#c9b63a 45%,#e8e0a0 65%,#5f6a30)"></div>
  </article>
  <article class="product" style="left:784px">
    <h3>Polepull</h3>
    <p>Lorem Ipsum is simply dummy text of the printing and type setting industry. Lorem Ipsum has been the industry's</p>
    <div class="product-photo" role="img" aria-label="Photo of athletes training on ski ergometers in a gym" style="background:linear-gradient(#b9aa98,#6b5e52)"></div>
  </article>
</body>
</html>
```